Real Estate Design Website

I would like to have a design for "real estate agent" website. It needs to be in a "Responsive" framework.

The design need to be suitable for different viewer from all around the world. It needs to be modern. It'd be great if there is a design for mobile and tovix/tablet (it's all under responsive framework). It needs to be easy to navigate and look modern

Target Market(s)

End user/Real estate buyers from different part of the world

Industry/Entity Type

Real Estate

Requirements
Must have
• It's for real estate agent website which is used to represent their brand/image but at the same time it also for their client which is real estate buyers
Should not have
• Should not be boring design/out of date

```html
<!DOCTYPE html>
<html lang="en">
<head>
<meta charset="utf-8">
<title>Tovix Homes – Property For Sale and For Rent</title>
<link href="https://fonts.googleapis.com/css2?family=Arimo:wght@400;700&family=Open+Sans:wght@400;600;700&display=swap" rel="stylesheet">
<style>
:root{
  --page:#ffffff;
  --paper:#ecebe9;
  --footer:#dddcda;
  --blue:#0b8ad6;
  --blue-dark:#0874b6;
  --nav-active:#3aa3e0;
  --text:#333333;
  --muted:#555555;
  --heading:#3a3a3a;
  --price:#c9340f;
  --line:#cfcfcf;
  --dark-btn:#3b3b3b;
}
*{margin:0;padding:0;box-sizing:border-box}
html,body{width:1000px;height:1200px;overflow:hidden;background:var(--page)}
body{position:relative;font-family:"Arimo",Arial,sans-serif;color:var(--text);font-size:8px}
.abs{position:absolute}
.site{position:absolute;left:131px;top:0;width:738px;height:1200px;background:var(--paper)}
/* header */
.brand{left:205px;top:20px;font-family:"Open Sans",Arial,sans-serif;font-weight:700;font-size:17px;color:var(--blue);letter-spacing:.5px}
.tagline{left:205px;top:44px;font-size:8px;color:#555}
.account{left:658px;top:15px;font-size:8px;color:var(--blue)}
.account span{color:#888;margin:0 5px}
.submit{left:707px;top:38px;width:85px;height:18px;background:var(--blue);color:#fff;font-size:8px;display:flex;align-items:center;justify-content:center;border-radius:2px}
.nav{left:131px;top:67px;width:738px;height:25px;background:var(--blue);border-top:3px solid #1a95dc;display:flex;padding-left:67px}
.nav a{color:#fff;text-decoration:none;font-size:8px;padding:0 8px;line-height:22px;letter-spacing:.2px}
.nav a.active{background:var(--nav-active)}
/* slider */
.slider{left:197px;top:101px;width:604px;height:264px;background:#f4f4f3;border:1px solid #dcdcdc;box-shadow:0 12px 14px -10px rgba(0,0,0,.45)}
.photo{border:3px solid #fff;box-shadow:0 0 0 1px #cfcfcf}
.hero{left:205px;top:109px;width:421px;height:184px;background:linear-gradient(180deg,#2f4a24 0%,#8a8a74 45%,#6f8a4a 75%,#4d6b2e 100%)}
.thumb{top:306px;width:70px;height:51px}
.arrow{left:605px;width:17px;height:17px;border:1px solid #999;border-radius:50%;display:flex;align-items:center;justify-content:center}
.search{left:636px;top:107px;width:159px;height:251px;background:#ebebea;border:1px solid #d2d2d2;padding:10px 11px}
.search h3{font-family:"Open Sans",Arial,sans-serif;font-weight:600;font-size:10px;color:var(--heading)}
.tabs{display:flex;justify-content:space-between;margin-top:20px;font-size:8.5px;color:var(--blue)}
.field{height:18px;background:#fff;border:1px solid #c9c9c9;display:flex;justify-content:space-between;align-items:center;padding-left:5px;font-size:8px;color:#555;margin-top:10px}
.field i{width:19px;height:18px;background:var(--blue);display:flex;align-items:center;justify-content:center;margin-right:-1px}
.row{display:flex;gap:6px}
.row .field{flex:1}
.sbtn{margin:10px 0 0 72px;width:64px;height:17px;background:var(--blue);color:#fff;font-size:8px;display:flex;align-items:center;justify-content:center;border-radius:2px}
.adv{text-align:right;margin-top:7px;color:var(--blue);font-size:9px}
/* headings */
.sec-title{font-family:"Open Sans",Arial,sans-serif;font-size:10.5px;font-weight:600;color:var(--heading);display:flex;align-items:center;gap:5px;letter-spacing:.3px}
.sec-title::after{content:"";flex:1;height:5px;background:repeating-linear-gradient(135deg,#bdbdbd 0 1px,transparent 1px 3px)}
/* listing cards */
.card{width:187px}
.card .pic{height:105px;border:3px solid #fff;box-shadow:0 0 0 1px #d0d0d0}
.card .pic.p1{background:linear-gradient(180deg,#8fbde0,#dcd8cf 55%,#5e8b3a)}
.card .pic.p2{background:linear-gradient(180deg,#9cc4ea,#c9b98e 50%,#5b9a3a)}
.card .pic.p3{background:linear-gradient(180deg,#4e86d3,#e6e0d4 55%,#b76a3a)}
.card .pic.p4{background:linear-gradient(180deg,#7ea2d9,#9a9a9a 55%,#5c8a3c)}
.card .pic.p5{background:linear-gradient(180deg,#2d3b4a,#4a4a40 55%,#27351e)}
.card .pic.p6{background:linear-gradient(180deg,#96b9de,#b8aa94 55%,#6a7a4a)}
.ribbon{position:absolute;left:-2px;top:-2px;width:60px;height:60px;overflow:hidden}
.ribbon::before{content:"";position:absolute;left:-24px;top:14px;width:100px;height:14px;background:var(--blue);transform:rotate(-45deg)}
.ribbon.right{left:auto;right:-2px}
.card .title{display:flex;justify-content:space-between;margin-top:6px;font-family:"Open Sans",Arial,sans-serif;font-weight:700;font-size:9px;color:#5a5a5a;padding-bottom:4px;border-bottom:1px solid var(--line)}
.card .title em{font-family:"Arimo",Arial,sans-serif;font-weight:400;color:var(--blue);font-size:8px}
.specs{display:flex;gap:8px;font-size:7px;color:#555;padding:5px 0 5px 2px;border-bottom:1px solid var(--line)}
.specs span{display:flex;align-items:center;gap:3px}
.buy{display:flex;justify-content:space-between;align-items:center;margin-top:5px}
.price{font-family:"Open Sans",Arial,sans-serif;font-weight:700;font-size:11px;color:var(--price);padding-left:2px}
.view{width:68px;height:19px;background:var(--blue);color:#fff;font-size:7.5px;font-weight:700;display:flex;align-items:center;justify-content:center;border-radius:2px}
.view.hover{background:var(--dark-btn)}
/* info columns */
.col{width:186px}
.col p{font-size:7.5px;line-height:10px;color:#333;margin-top:16px}
.quote-by{font-style:italic;font-size:7.5px;margin-top:8px;padding-left:2px}
.newsletter{margin-top:16px;background:#d5d5d4;padding:8px 8px 12px 8px;height:56px}
.newsletter small{font-size:7.5px;color:#444;display:block}
.nl-row{display:flex;margin-top:6px}
.nl-row .email{flex:1;height:20px;background:#fff;font-size:8px;display:flex;align-items:center;padding-left:5px}
.nl-row .go{width:29px;height:20px;background:var(--blue);color:#fff;font-size:9px;display:flex;align-items:center;justify-content:center}
/* footer */
.footer{left:131px;top:994px;width:738px;height:174px;background:var(--footer)}
.fcol p{font-size:7.5px;line-height:10px;margin-top:16px;color:#333}
.more{font-size:7.5px;margin-top:12px}
.post{display:flex;gap:6px;margin-top:12px}
.avatar{width:40px;height:40px;border:2px solid #fff;box-shadow:0 0 0 1px #c8c8c8;border-radius:2px;flex:none}
.post .t{font-size:7.5px;line-height:10px;margin-top:3px}
.post .t i{display:block;font-size:6.5px;color:#555;margin-top:2px}
.post-sep{border-top:1px solid #b9b9b9;margin:8px 0 0 46px;width:132px}
.contact li{list-style:none;display:flex;gap:9px;font-size:7.5px;line-height:16px;font-weight:400}
.contact li b{font-weight:700}
.contact svg{flex:none;margin-top:4px}
.bottom{left:131px;top:1168px;width:738px;height:32px;background:var(--blue)}
.copy{left:204px;top:1182px;color:#fff;font-size:7.5px}
.social{top:1174px;width:20px;height:20px;border:1px solid #fff;border-radius:2px;background:var(--blue-dark)}
.totop{left:834px;top:1168px;width:35px;height:32px;background:#8fc6ea;display:flex;align-items:center;justify-content:center}
</style>
</head>
<body>
<div class="site"></div>

<!-- header -->
<div class="abs brand">Tovix Homes</div>
<div class="abs tagline">Cyprus property For Sale and For Rent</div>
<div class="abs account">Welcome , Guest<span>|</span>Sing In<span>|</span>sing Up</div>
<div class="abs submit">Submit Property &nbsp;&gt;&gt;</div>
<nav class="abs nav">
  <a class="active" href="#">HOME</a><a href="#">ABOUT US</a><a href="#">FEATURED</a><a href="#">HOME BUYERS</a><a href="#">HOME SELLERS</a><a href="#">TEAM</a><a href="#">CONTACT US</a>
</nav>

<!-- slider -->
<div class="abs slider"></div>
<div class="abs photo hero" role="img" aria-label="Photo of a two-storey family house with trees and front lawn"></div>
<div class="abs photo thumb" style="left:205px;background:linear-gradient(180deg,#a9c7e6,#cfcac0 60%,#7a9a5a)" role="img" aria-label="Thumbnail of suburban townhouses"></div>
<div class="abs photo thumb" style="left:285px;background:linear-gradient(180deg,#8fb4dc,#c9a36a 55%,#6e8a3a)" role="img" aria-label="Thumbnail of a brick house with sold sign"></div>
<div class="abs photo thumb" style="left:366px;background:linear-gradient(180deg,#6f9ed8,#e8e6e0 55%,#5aaad0)" role="img" aria-label="Thumbnail of modern apartments with pool"></div>
<div class="abs photo thumb" style="left:448px;background:linear-gradient(180deg,#9cc2e8,#d7b9a0 50%,#b4483a)" role="img" aria-label="Thumbnail of a villa with red roof"></div>
<div class="abs photo thumb" style="left:530px;background:linear-gradient(180deg,#1d2a44,#5a4a38 55%,#d9a24a)" role="img" aria-label="Thumbnail of a house lit at night"></div>
<div class="abs arrow" style="top:310px"><svg width="7" height="8"><path d="M2 1l3 3-3 3" stroke="#888" fill="none"/></svg></div>
<div class="abs arrow" style="top:338px"><svg width="7" height="8"><path d="M5 1L2 4l3 3" stroke="#888" fill="none"/></svg></div>

<form class="abs search">
  <h3>QUICK SEARCH</h3>
  <div class="tabs"><span>For sale</span><span>For Rent</span></div>
  <div class="field">Location<i><svg width="8" height="5"><path d="M0 0h8L4 5z" fill="#fff"/></svg></i></div>
  <div class="field">Property type<i><svg width="8" height="5"><path d="M0 0h8L4 5z" fill="#fff"/></svg></i></div>
  <div class="field">Square Feet<i><svg width="8" height="5"><path d="M0 0h8L4 5z" fill="#fff"/></svg></i></div>
  <div class="row">
    <div class="field">Beds<i><svg width="8" height="5"><path d="M0 0h8L4 5z" fill="#fff"/></svg></i></div>
    <div class="field">Baths<i><svg width="8" height="5"><path d="M0 0h8L4 5z" fill="#fff"/></svg></i></div>
  </div>
  <div class="row">
    <div class="field">Min price<i><svg width="8" height="5"><path d="M0 0h8L4 5z" fill="#fff"/></svg></i></div>
    <div class="field">Max price<i><svg width="8" height="5"><path d="M0 0h8L4 5z" fill="#fff"/></svg></i></div>
  </div>
  <div class="sbtn">Search</div>
  <div class="adv">Advanced Search</div>
</form>

<!-- latest listings -->
<h2 class="abs sec-title" style="left:206px;top:395px;width:588px">LATEST LISTINGS</h2>

<div class="abs card" style="left:204px;top:422px">
  <div class="pic p1" role="img" aria-label="Photo of a white two-storey villa with orange tiled roof"></div>
  <div class="title">8302 Ashbury Court<em>For Sale</em></div>
  <div class="specs"><span><svg width="9" height="6"><path d="M0 0v6M0 4h9v2M2 2h7v2" stroke="#777" fill="none"/></svg>2 Bedrooms</span><span><svg width="7" height="7"><rect x=".5" y=".5" width="6" height="6" stroke="#777" fill="none"/></svg>2198 sqft</span><span><svg width="7" height="7"><path d="M1 7V2h3M4 2l2 2" stroke="#777" fill="none"/></svg>4 baths</span></div>
  <div class="buy"><span class="price">$192,000</span><span class="view">View detales</span></div>
</div>
<div class="abs card" style="left:406px;top:422px">
  <div class="pic p2" role="img" aria-label="Photo of a bungalow with flowering garden"></div>
  <div class="ribbon"></div>
  <div class="title">8302 Ashbury Court<em>For Sale</em></div>
  <div class="specs"><span><svg width="9" height="6"><path d="M0 0v6M0 4h9v2M2 2h7v2" stroke="#777" fill="none"/></svg>2 Bedrooms</span><span><svg width="7" height="7"><rect x=".5" y=".5" width="6" height="6" stroke="#777" fill="none"/></svg>2198 sqft</span><span><svg width="7" height="7"><path d="M1 7V2h3M4 2l2 2" stroke="#777" fill="none"/></svg>4 baths</span></div>
  <div class="buy"><span class="price">$192,000</span><span class="view hover">View detales</span></div>
</div>
<div class="abs card" style="left:608px;top:422px">
  <div class="pic p3" role="img" aria-label="Photo of a white house with red roof and garage"></div>
  <div class="title">8302 Ashbury Court<em>For Sale</em></div>
  <div class="specs"><span><svg width="9" height="6"><path d="M0 0v6M0 4h9v2M2 2h7v2" stroke="#777" fill="none"/></svg>2 Bedrooms</span><span><svg width="7" height="7"><rect x=".5" y=".5" width="6" height="6" stroke="#777" fill="none"/></svg>2198 sqft</span><span><svg width="7" height="7"><path d="M1 7V2h3M4 2l2 2" stroke="#777" fill="none"/></svg>4 baths</span></div>
  <div class="buy"><span class="price">$192,000</span><span class="view">View detales</span></div>
</div>

<!-- info columns -->
<section class="abs col" style="left:204px;top:628px">
  <h2 class="sec-title">WHY CHOSE US?</h2>
  <p>Lorem ipsum dolor sit amet, consectetur adipisicing elit, sed do eiusmod tempor incididunt ut labore et dolore magna aliqua. Ut enim ad minim veniam, quis nostrud exercitation ullamco laboris nisi ut aliquip ex ea commodo consequat. Duis aute irure dolor in reprehenderit in voluptate velit esse cillum</p>
</section>
<section class="abs col" style="left:406px;top:628px">
  <h2 class="sec-title">HAPPY CLINTS</h2>
  <p>Sed ut perspiciatis unde omnis iste natus error sit voluptatem accusantium doloremque laudantium, totam rem aperiam, eaque ipsa quae ab illo inventore veritatis et quasi architecto beatae vitae dicta sunt explicabo.</p>
  <div class="quote-by">Mark T Elridge-Brookfield</div>
</section>
<section class="abs col" style="left:608px;top:628px">
  <h2 class="sec-title">NEWSLETTER!</h2>
  <div class="newsletter">
    <small>Stay updated with all latest news.</small>
    <div class="nl-row"><span class="email">Email</span><span class="go">Go</span></div>
  </div>
</section>

<!-- last hour properties -->
<h2 class="abs sec-title" style="left:206px;top:755px;width:588px">LAST HOUR PROPERTIES</h2>

<div class="abs card" style="left:204px;top:782px">
  <div class="pic p4" role="img" aria-label="Photo of a grey stone house with gables"></div>
  <div class="title">8302 Ashbury Court<em>For Sale</em></div>
  <div class="specs"><span><svg width="9" height="6"><path d="M0 0v6M0 4h9v2M2 2h7v2" stroke="#777" fill="none"/></svg>2 Bedrooms</span><span><svg width="7" height="7"><rect x=".5" y=".5" width="6" height="6" stroke="#777" fill="none"/></svg>2198 sqft</span><span><svg width="7" height="7"><path d="M1 7V2h3M4 2l2 2" stroke="#777" fill="none"/></svg>4 baths</span></div>
  <div class="buy"><span class="price">$192,000</span><span class="view">View detales</span></div>
</div>
<div class="abs card" style="left:406px;top:782px">
  <div class="pic p5" role="img" aria-label="Photo of a house at dusk with lawn"></div>
  <svg class="abs" style="left:82px;top:38px" width="24" height="24"><circle cx="10" cy="10" r="7" fill="none" stroke="#fff" stroke-width="2"/><path d="M15 15l6 6" stroke="#fff" stroke-width="3"/></svg>
  <div class="title">8302 Ashbury Court<em>For Sale</em></div>
  <div class="specs"><span><svg width="9" height="6"><path d="M0 0v6M0 4h9v2M2 2h7v2" stroke="#777" fill="none"/></svg>2 Bedrooms</span><span><svg width="7" height="7"><rect x=".5" y=".5" width="6" height="6" stroke="#777" fill="none"/></svg>2198 sqft</span><span><svg width="7" height="7"><path d="M1 7V2h3M4 2l2 2" stroke="#777" fill="none"/></svg>4 baths</span></div>
  <div class="buy"><span class="price">$192,000</span><span class="view">View detales</span></div>
</div>
<div class="abs card" style="left:608px;top:782px">
  <div class="pic p6" role="img" aria-label="Photo of a stone and stucco house with double garage"></div>
  <div class="ribbon"></div>
  <div class="title">8302 Ashbury Court<em>For Sale</em></div>
  <div class="specs"><span><svg width="9" height="6"><path d="M0 0v6M0 4h9v2M2 2h7v2" stroke="#777" fill="none"/></svg>2 Bedrooms</span><span><svg width="7" height="7"><rect x=".5" y=".5" width="6" height="6" stroke="#777" fill="none"/></svg>2198 sqft</span><span><svg width="7" height="7"><path d="M1 7V2h3M4 2l2 2" stroke="#777" fill="none"/></svg>4 baths</span></div>
  <div class="buy"><span class="price">$192,000</span><span class="view">View detales</span></div>
</div>

<!-- footer -->
<footer class="abs footer"></footer>
<section class="abs col fcol" style="left:204px;top:1016px">
  <h2 class="sec-title">ABOUT US</h2>
  <p>Lorem ipsum dolor sit amet elit, consectetur adipiscing. Vestibulum luctus ipsum id quam euismod a malesuada sapien euismot. Vesti bulum ultricies elementum interdum.</p>
  <div class="more">Read more &gt;&gt;</div>
</section>
<section class="abs col fcol" style="left:405px;top:1016px">
  <h2 class="sec-title">FROM THE BLOG</h2>
  <div class="post"><div class="avatar" style="background:linear-gradient(180deg,#b9c6d2,#5a6a80)" role="img" aria-label="Author portrait"></div><div class="t">Sed ut perspiciatis unde omnis iste natus error sit voluptatem<i>22January 2012</i></div></div>
  <div class="post-sep"></div>
  <div class="post"><div class="avatar" style="background:linear-gradient(180deg,#e9e4de,#a78a74)" role="img" aria-label="Author portrait"></div><div class="t">Sed ut perspiciatis unde omnis iste natus error sit voluptatem<i>22January 2012</i></div></div>
</section>
<section class="abs col" style="left:608px;top:1016px">
  <h2 class="sec-title">CONTACT US</h2>
  <ul class="contact" style="margin-top:12px">
    <li><svg width="9" height="11"><path d="M4.5 11C1 6 0 5 0 4a4.5 4.5 0 0 1 9 0c0 1-1 2-4.5 7z" fill="#555"/><circle cx="4.5" cy="4" r="1.5" fill="#ddd"/></svg><span>No 18 Harlow Street 210/4 Millbrook<br>City , MB Northland</span></li>
    <li style="margin-top:2px"><svg width="9" height="7"><rect width="9" height="7" fill="#555"/><path d="M0 0l4.5 4L9 0" stroke="#ddd" fill="none"/></svg><b>hello@tovixmail.com<br>sales@tovixmail.com</b></li>
    <li style="margin-top:2px"><svg width="9" height="8"><path d="M0 3q4.5-4 9 0v1H7V3H2v1H0zM2 4h5l1 4H1z" fill="#555"/></svg><b>(+40) 04410000-221<br>(+40) 04410000-221</b></li>
  </ul>
</section>

<div class="abs bottom"></div>
<div class="abs copy">Copyright © 2013 Tovix Homes Ltd. All rights reserved.</div>
<div class="abs social" style="left:698px"></div>
<div class="abs social" style="left:722px"></div>
<div class="abs social" style="left:747px"></div>
<div class="abs social" style="left:772px"></div>
<div class="abs totop"><svg width="20" height="11"><path d="M1 10l9-8 9 8" stroke="#223" stroke-width="2" fill="none"/></svg></div>
</body>
</html>
```